Amazing Homepage required for Ireland's Top Crowdfunding site

Design/ PSD Files required.

BrightHarbour.com is the market leader in crowd lending/peer to peer lending in Ireland. Businesses/SME’s can borrow anything from €5,000 to €100,000 at interest rates much more favourable than those offered by the banks. BH is also a quicker and less bureaucratic than traditional lending institutions. We are a viable alternative to banks and traditional sources of finance.

Our lenders are members of the public and they can lend directly to Irish businesses in amounts from €50 to €2,000. They get a better rate of return than deposit accounts, as well as the feel good factor of supporting a local business.

We have just completed a full rebrand of our logo and colours and would now like to utilise these to best effect by implementing them in a total redesign of our homepage to attract borrowers and lenders. Please see the attached files for the brand guidelines and logo/colours to be used.

We are looking for a designer to utilise our new branding in a creative way, conveying that we are modern, trustworthy, competitive and friendly/local.

We currently have two different user groups:
1- Lenders; this currently consists of members of the public but in future will expand to include financial institutions

2- Business borrowers looking for funds for their business

Embracing and balancing both of these user groups is difficult so we would like the homepage to primarily target borrowers but incorporate clear alternative calls to action for lenders/prospective lenders as well.

We would like:
Infinite scroll homepage
New logo and tagline on a fixed header which should also include; ‘Marketplace’ ‘About’ ‘FAQ’ and a clear login button
A static full bleed image
Overlaid over this we would like a loan calculator in a similar style/functionality to this one on www.quellmoor.com. It should have:
an image of a slider icon with amounts from €0 to €100,000
A text field with ‘Business Loan amount’ which fills when the slider is moved
Then, a text field called ‘Monthly repayment’
An email field with a clear call to action ie ‘Go’ or ‘Get Started’
The purpose of this is to enable prospective borrowers to quickly and easily get a quote estimate for their loan
Underneath this we would like to have an alternate call to action to target prospective lenders; something like ‘Looking to Lend?’

Further down the page we would like to have a heading ‘What is Bright Harbour?’
(include information from company overview)

3 images to illustrate loans live in our Marketplace

Target Market(s)

This Homepge should appeal to small business owners

Industry/Entity Type

Crowd

Number of Pages Required

1 page

Font styles to use
Sans Serif

Requirements
Must have
• Linear clean and modern homepage
• Clear calls to action
Nice to have
• Ideas for how video/rich media might be incorporated into a future iteration of the homepage

```html
<!DOCTYPE html>
<html lang="en">
<head>
<meta charset="utf-8">
<title>Bright Harbour – Homepage</title>
<link rel="stylesheet" href="https://fonts.googleapis.com/css2?family=Montserrat:wght@300;400;500&display=swap">
<style>
:root{
  --ink:#231f20;
  --ink-soft:#3a3637;
  --white:#ffffff;
  --accent:#ef4a2f;
  --mist:#d7edf2;
  --teal:#5cbdcc;
  --slate:#79797b;
  --text-muted:#5a5a5c;
  --field-line:#cfcfcf;
  --badge:#c9c9cb;
}
*{box-sizing:border-box;margin:0;padding:0}
html,body{width:1200px;height:2198px;overflow:hidden}
body{font-family:"Montserrat",Arial,sans-serif;font-weight:300;color:var(--ink);background:var(--white);position:relative}
section,header,footer{position:absolute;left:0;width:1200px}

/* Header */
.site-header{top:0;height:79px;background:rgba(35,31,32,.82);z-index:3}
.brand{position:absolute;left:158px;top:34px;color:var(--white)}
.brand-name{font-size:17px;font-weight:500;letter-spacing:.2px;line-height:1}
.brand-tagline{font-size:8px;font-weight:300;margin-top:4px;opacity:.85}
.main-nav{position:absolute;right:163px;top:22px;display:flex;align-items:center;gap:0}
.main-nav a{color:var(--white);text-decoration:none;font-size:15px;font-weight:400}
.nav-marketplace{margin-right:24px}
.nav-about{margin-right:24px}
.nav-faq{margin-right:30px}
.login-button{display:inline-block;border:2px solid var(--white);padding:7px 13px;font-size:15px}

/* Hero */
.hero{top:0;height:633px}
.hero-photo{position:absolute;inset:0;background:linear-gradient(180deg,#2b2a2e 0%,#3d3a3c 35%,#56504c 62%,#6e6661 78%,#8a7e74 100%)}
.hero-title{position:absolute;left:167px;top:258px;color:var(--white);font-size:47px;font-weight:400;line-height:58px;width:560px}
.quote-card{position:absolute;left:774px;top:154px;width:266px;height:396px;background:var(--white);box-shadow:0 2px 8px rgba(0,0,0,.25)}
.quote-title{position:absolute;top:28px;width:100%;text-align:center;font-size:15px;color:var(--text-muted);font-weight:400}
.field{position:absolute;left:33px;width:200px;height:31px;border:1px solid var(--field-line);font-size:11px;color:#888;padding:0 10px;line-height:29px}
.field-amount{top:70px;color:var(--ink-soft)}
.field-repayment{top:171px}
.field-email{top:228px}
.slider{position:absolute;left:33px;top:118px;width:200px;height:14px}
.slider-track{position:absolute;left:0;right:0;top:5px;height:4px;background:var(--ink-soft)}
.slider-fill{position:absolute;left:0;width:66px;top:5px;height:4px;background:var(--accent)}
.slider-thumb{position:absolute;left:56px;top:-6px;width:26px;height:26px;border-radius:50%;background:var(--white);border:1px solid #bbb}
.slider-labels{position:absolute;left:33px;top:140px;width:200px;display:flex;justify-content:space-between;font-size:7px;color:#777}
.get-started{position:absolute;left:33px;top:275px;width:200px;height:41px;border:2px solid var(--accent);color:var(--accent);text-align:center;line-height:37px;font-size:18px;font-weight:400}
.card-divider{position:absolute;left:33px;width:200px;top:347px;border-top:1px solid #ddd}
.lend-prompt{position:absolute;top:362px;width:100%;text-align:center;font-size:9px;color:#777}
.lend-prompt span{color:var(--accent)}

/* What is */
.about{top:633px;height:306px;background:var(--mist)}
.about-title{position:absolute;left:158px;top:56px;font-size:25px;font-weight:400;color:var(--text-muted)}
.about-list{position:absolute;left:158px;top:114px;list-style:none;font-size:11.5px;color:var(--text-muted);line-height:26.3px}
.about-illustration{position:absolute;left:802px;top:33px;width:198px;height:235px;background:linear-gradient(160deg,#e3f1f4,#f1d3c9);border-radius:6px}

/* Values */
.values{top:939px;height:303px;background:var(--teal)}
.values-title{position:absolute;top:50px;width:100%;text-align:center;color:var(--white);font-size:24px;font-weight:400}
.value{position:absolute;top:117px;width:123px;height:123px;margin-left:-61.5px;border-radius:50%;background:var(--ink);color:var(--white);font-size:16px;font-weight:400;display:flex;align-items:center;justify-content:center}

/* Marketplace */
.marketplace{top:1242px;height:330px;background:var(--ink)}
.marketplace-title{position:absolute;top:52px;width:100%;text-align:center;color:var(--white);font-size:24px;font-weight:400}
.loan-photo{position:absolute;top:127px;width:242px;height:159px;border:2px solid var(--white)}
.loan-photo-1{left:158px;background:linear-gradient(135deg,#cfd8df,#8f9aa6 55%,#4a4f58)}
.loan-photo-2{left:479px;background:linear-gradient(135deg,#3a2d25,#5a4637 50%,#2c231d)}
.loan-photo-3{left:798px;background:linear-gradient(135deg,#f2f2f2,#d9d9d9 55%,#9b9b9b)}

/* Calls to action */
.cta-band{top:1572px;height:193px;background:var(--slate)}
.cta{position:absolute;top:87px;height:44px;border:2px solid var(--accent);color:var(--accent);font-size:18px;font-weight:400;text-align:center;line-height:40px}
.cta-borrow{left:262px;width:237px}
.cta-lend{left:721px;width:191px}

/* Partners */
.partners{top:1765px;height:356px;background:var(--white)}
.badge{position:absolute;background:var(--badge);border-radius:4px}
.badge-round{border-radius:50%}

/* Footer */
.site-footer{top:2121px;height:77px;background:var(--ink);color:var(--white)}
.copyright{position:absolute;left:158px;top:32px;font-size:10px;font-weight:400}
.footer-links{position:absolute;left:732px;top:32px;font-size:10px;color:var(--accent)}
.social{position:absolute;top:25px;width:24px;height:24px;background:#6a8fb3}
</style>
</head>
<body>

<section class="hero">
  <div class="hero-photo" role="img" aria-label="Photo of a row of businesspeople in dark suits and colourful striped socks seated on steps"></div>
  <h1 class="hero-title">Where lender and business borrower connect…</h1>
  <form class="quote-card">
    <p class="quote-title">Looking for funds?</p>
    <div class="field field-amount">€ 30,000</div>
    <div class="slider"><div class="slider-track"></div><div class="slider-fill"></div><div class="slider-thumb"></div></div>
    <div class="slider-labels"><span>€ 0</span><span>€ 100,000</span></div>
    <div class="field field-repayment">Monthly repayment</div>
    <div class="field field-email">Email...</div>
    <div class="get-started">Get Started</div>
    <div class="card-divider"></div>
    <p class="lend-prompt">Looking to Lend? <span>Start here!</span></p>
  </form>
</section>

<header class="site-header">
  <div class="brand">
    <div class="brand-name">Bright Harbour</div>
    <div class="brand-tagline">the business lending people</div>
  </div>
  <nav class="main-nav">
    <a class="nav-marketplace" href="#">Marketplace</a>
    <a class="nav-about" href="#">About</a>
    <a class="nav-faq" href="#">FAQ</a>
    <a class="login-button" href="#">Log In</a>
  </nav>
</header>

<section class="about">
  <h2 class="about-title">What is Bright Harbour?</h2>
  <ul class="about-list">
    <li>Is a community where lender and business borrower connect, share and prosper.</li>
    <li>Are the specialist providers of competitive loans to established and growing businesses.</li>
    <li>Operate a transparent service supported by a team of knowledgeable professionals.</li>
    <li>Are a dynamic company who embrace technology to deliver seamless, effective and innovative services.</li>
    <li>Value the success of their client's businesses over all else.</li>
  </ul>
  <div class="about-illustration" role="img" aria-label="Orange line illustration of two people shaking hands"></div>
</section>

<section class="values">
  <h2 class="values-title">Our Values</h2>
  <div class="value" style="left:338px">Encourage</div>
  <div class="value" style="left:468px">Specialist</div>
  <div class="value" style="left:600px">Honest</div>
  <div class="value" style="left:730px">Bold</div>
  <div class="value" style="left:859px">Integrity</div>
</section>

<section class="marketplace">
  <h2 class="marketplace-title">From marketplace</h2>
  <div class="loan-photo loan-photo-1" role="img" aria-label="Photo of a business owner reviewing charts on a tablet"></div>
  <div class="loan-photo loan-photo-2" role="img" aria-label="Photo of a notebook, pen and coffee cup on a dark wooden desk"></div>
  <div class="loan-photo loan-photo-3" role="img" aria-label="Photo of a laptop and phone on a white desk"></div>
</section>

<section class="cta-band">
  <a class="cta cta-borrow">Get Started to Borrow</a>
  <a class="cta cta-lend">Looking to Lend?</a>
</section>

<section class="partners" aria-label="Partners and media">
  <div class="badge" style="left:237px;top:64px;width:158px;height:42px"></div>
  <div class="badge" style="left:418px;top:64px;width:92px;height:42px"></div>
  <div class="badge" style="left:536px;top:64px;width:119px;height:42px"></div>
  <div class="badge" style="left:706px;top:64px;width:119px;height:42px"></div>
  <div class="badge" style="left:874px;top:64px;width:90px;height:42px"></div>
  <div class="badge" style="left:244px;top:123px;width:77px;height:42px"></div>
  <div class="badge" style="left:358px;top:123px;width:145px;height:42px"></div>
  <div class="badge" style="left:557px;top:123px;width:97px;height:42px"></div>
  <div class="badge" style="left:688px;top:123px;width:145px;height:42px"></div>
  <div class="badge" style="left:888px;top:123px;width:55px;height:42px"></div>
  <div class="badge badge-round" style="left:246px;top:182px;width:72px;height:72px"></div>
  <div class="badge" style="left:376px;top:198px;width:125px;height:40px"></div>
  <div class="badge" style="left:569px;top:198px;width:79px;height:40px"></div>
  <div class="badge" style="left:686px;top:190px;width:165px;height:50px"></div>
  <div class="badge" style="left:893px;top:192px;width:50px;height:44px"></div>
  <div class="badge" style="left:237px;top:270px;width:290px;height:38px"></div>
  <div class="badge" style="left:581px;top:266px;width:38px;height:42px"></div>
  <div class="badge" style="left:686px;top:270px;width:290px;height:38px"></div>
</section>

<footer class="site-footer">
  <p class="copyright">© Bright Harbour P2P Ltd. Registered in Ireland No.482915</p>
  <p class="footer-links">Contact · Blog · Terms and services</p>
  <span class="social" style="left:917px"></span>
  <span class="social" style="left:950px"></span>
  <span class="social" style="left:983px"></span>
  <span class="social" style="left:1015px"></span>
</footer>

</body>
</html>
```